Label design for ecological olive oil from an innovative farm in Spain

EL PRADO SOLAR - Olive Oil Label
El Prado Solar is a small farm in southern Spain dedicated to regenerative, ecological and syntropic agriculture. We are launching a new extra virgin olive oil and, alongside it, a renewed brand identity that reflects our relationship with land, life and earth.
Our farm works as a living food forest: diverse, dense, colourful and abundant. This is not industrial organic farming — it is ecosystem regeneration in action. We are looking for a label that feels:
* Lush, abundant and alive
* Nature-connected and animist (the land as a living being)
* Sunny Mediterranean (southern Spain, warmth, light, joy)
* Upbeat and playful, not austere or “eco-serious”
* Slightly rebellious, non-corporate, non-industrial
This is an olive oil for people who care deeply about the planet, but who also love beauty, colour and pleasure.
We are particularly drawn to designs that express the visual richness and lushness of our syntropic food forest:
* Dense, layered plant life
* Multiple tree species growing together
* A sense of abundance
* A “window into a living world” feeling
Tree species present on the farm include:
* Olive
* Citrus
* Pomegranate
* Fig
* Almond
We welcome designs with illustrative approaches that feel hand-drawn, painterly or slightly retro. We are open to interpretation — the goal is to transmit aliveness, not literal realism.
We currently use Montserrat font and are happy to continue with it or something similar.
We are also open to retro-inspired or softer typefaces, provided they feel natural, warm and not corporate.
We want to avoid plastic labels. The design should work with:
* Uncoated/organic paper labels, or
* Direct printing or screen printing onto glass
The label should feel tactile and natural.
We have uploaded :
* Final front and back label text (Spanish + English)
* Logo
* Reference images (AI explorations, farm photos, landscape, food forest)
The olive oil will be sold in Spain and internationally, so bilingual clarity is important.
Our business logo should be used but does not need to dominate the front label.
It may work better subtly placed, possibly on the back label or integrated quietly into the design.
A successful label will feel like:
* A living landscape captured on a bottle
* Something joyful, rooted and contemporary
* A product of land, care and imagination — not marketing
We want people to feel, instinctively:
This oil comes from a place that is alive.

```html
<!DOCTYPE html>
<html lang="es">
<head>
<meta charset="utf-8">
<title>El Prado Solar – Etiquetas de aceite</title>
<link rel="stylesheet" href="https://fonts.googleapis.com/css2?family=Crimson+Text:ital,wght@0,400;0,600;1,400&family=Cinzel:wght@600&display=swap">
<style>
:root{
  --stage:#e6e6e8;
  --wine-top:#130406;
  --wine-mid:#2a0608;
  --wine-bottom:#730b08;
  --gold:#e9c25c;
  --gold-deep:#c9962f;
  --gold-pale:#f6ebc4;
  --cream:#f3e6c7;
  --olive:#8ea43a;
  --olive-pale:#d4d98a;
  --amber:#e9b86a;
}
*{margin:0;padding:0;box-sizing:border-box}
html,body{width:1200px;height:843px;overflow:hidden;background:var(--stage)}
.canvas{position:relative;width:1200px;height:843px;font-family:"Crimson Text",serif}
.label{position:absolute;color:var(--cream);text-align:center}
.label-frame{position:absolute;inset:0;width:100%;height:100%}
.label-front{left:150px;top:34px;width:384px;height:776px}
.label-back{left:680px;top:50px;width:360px;height:746px}
.label-content{position:absolute;inset:0}
.brand{position:absolute;left:0;right:0;color:var(--gold);font-weight:600;line-height:1}
.brand-front{top:58px;font-size:52px}
.brand-front .brand-line{display:block}
.product-title{position:absolute;left:0;right:0;top:196px;font-family:"Cinzel",serif;font-weight:600;font-size:44px;color:var(--olive-pale);letter-spacing:1px}
.artwork{position:absolute;left:50%;transform:translateX(-50%);border-radius:50% 50% 46% 46%}
.artwork-front{top:200px;width:300px;height:270px;background:radial-gradient(ellipse at 50% 55%,rgba(142,164,58,.55),rgba(90,110,30,.25) 55%,rgba(0,0,0,0) 72%)}
.artwork-back{top:80px;width:220px;height:180px;background:radial-gradient(ellipse at 50% 55%,rgba(142,164,58,.5),rgba(90,110,30,.2) 55%,rgba(0,0,0,0) 72%)}
.front-copy{position:absolute;left:0;right:0;top:505px}
.line{display:block}
.designation-es{color:var(--gold);font-size:16px;font-weight:600;margin-bottom:18px}
.designation-en,.practice-lead{font-size:16px;font-weight:600;color:var(--gold-pale);line-height:1.45}
.practice-es{color:var(--gold);font-size:21px;font-weight:600;margin-top:30px}
.practice-en{color:var(--amber);font-size:21px;line-height:1.5;margin-top:6px}
.volume{position:absolute;left:0;right:0;top:720px;font-size:34px;color:var(--gold-pale)}
.back-copy{position:absolute;left:26px;right:26px;top:290px;font-size:11px;line-height:1.45}
.back-copy p{margin-bottom:11px}
.back-copy strong{color:var(--gold);font-weight:600}
.back-copy em{color:var(--gold);font-style:italic}
.back-copy .block{margin-top:22px}
.back-copy .fine{font-size:7.5px;line-height:1.5;margin-bottom:7px}
.back-copy .fine-en{font-size:10px}
</style>
</head>
<body>
<main class="canvas">

  <section class="label label-front" aria-label="Etiqueta frontal">
    <svg class="label-frame" viewBox="0 0 384 776" preserveAspectRatio="none" aria-hidden="true">
      <defs>
        <linearGradient id="wineFront" x1="0" y1="0" x2="0" y2="1">
          <stop offset="0" stop-color="#130406"/>
          <stop offset=".5" stop-color="#2a0608"/>
          <stop offset="1" stop-color="#730b08"/>
        </linearGradient>
      </defs>
      <path d="M30,20 Q192,-10 354,20 Q354,50 384,50 L384,726 Q354,726 354,756 Q192,786 30,756 Q30,726 0,726 L0,50 Q30,50 30,20 Z" fill="#f6ebc4" stroke="#c9962f" stroke-width="3"/>
      <path transform="translate(13,13) scale(0.932,0.966)" d="M30,20 Q192,-10 354,20 Q354,50 384,50 L384,726 Q354,726 354,756 Q192,786 30,756 Q30,726 0,726 L0,50 Q30,50 30,20 Z" fill="url(#wineFront)" stroke="#e9c25c" stroke-width="2"/>
    </svg>
    <div class="label-content">
      <h1 class="brand brand-front"><span class="brand-line">El</span><span class="brand-line">Prado Solar</span></h1>
      <div class="artwork artwork-front" role="img" aria-label="Ilustración de ramas de olivo con aceitunas verdes y una gota de aceite"></div>
      <p class="product-title">OLIVE OILS</p>
      <div class="front-copy">
        <span class="line designation-es">Aceite de Oliva Virgen Extra</span>
        <span class="line designation-en">Extra Virgin Olive Oil</span>
        <span class="line practice-lead">Cultivado con practicas de la</span>
        <span class="line practice-es">agricultura regenerativa y sintrópica</span>
        <span class="line practice-en">Grown using regenerative and<br>syntropic farming practices</span>
      </div>
      <p class="volume">500ml</p>
    </div>
  </section>

  <section class="label label-back" aria-label="Etiqueta trasera">
    <svg class="label-frame" viewBox="0 0 360 746" preserveAspectRatio="none" aria-hidden="true">
      <defs>
        <linearGradient id="wineBack" x1="0" y1="0" x2="0" y2="1">
          <stop offset="0" stop-color="#130406"/>
          <stop offset=".5" stop-color="#2a0608"/>
          <stop offset="1" stop-color="#730b08"/>
        </linearGradient>
      </defs>
      <path d="M30,20 Q180,-10 330,20 Q330,50 360,50 L360,696 Q330,696 330,726 Q180,756 30,726 Q30,696 0,696 L0,50 Q30,50 30,20 Z" fill="#f6ebc4" stroke="#c9962f" stroke-width="3"/>
      <path transform="translate(13,13) scale(0.928,0.965)" d="M30,20 Q180,-10 330,20 Q330,50 360,50 L360,696 Q330,696 330,726 Q180,756 30,726 Q30,696 0,696 L0,50 Q30,50 30,20 Z" fill="url(#wineBack)" stroke="#e9c25c" stroke-width="2"/>
    </svg>
    <div class="label-content">
      <div class="artwork artwork-back" role="img" aria-label="Ilustración de ramas de olivo con aceitunas y una gota de aceite"></div>
      <div class="back-copy">
        <p>Aceite de oliva de categoría superior obtenido directamente de aceitunas y solo mediante procedimientos mecánicos.</p>
        <p>Origen: <strong>Valdelomas, Granada, España</strong></p>
        <p class="block">Edición limitada de la finca única<br>Elaborado y envasado por:<br><strong>Fundación El Prado Solar</strong><br><em>Proyecto agrícola dedicado a la regeneración de ecosistemas y al cuidado de la tierra y las personas.</em><br>Recolectado a mano</p>
        <p class="block fine-en">Prensado en frío, menos de un día<br>tras la cosecha</p>
        <p class="fine-en">Limited edition from a single farm<br>Produced and bottled by:<br><strong>Fundación El Prado Solar</strong><br><em>An agricultural project dedicated to ecosystem regeneration and the care of land and people.</em></p>
        <p class="fine">Hand picked and cold pressed<br>within one day of harvest</p>
        <p class="fine">Variedad: <strong>Picual · Manzanilla · Acebuche (Wild Olive)</strong><br>Sin filtrar<br>Conservar en lugar fresco y protegido de la luz.</p>
        <p class="fine">Lote: Otoño 2025<br>Consumir preferentemente antes de: 05/2027</p>
      </div>
    </div>
  </section>

</main>
</body>
</html>
```